Supplement Rebranding Bottle Design

READ WORD DOCUMENT ATTACHED.
We want to rebrand our current health supplements (see below). We do want it to be modern, vibrant and appealing. Very upscale and elegant as it targets primarily women.
Bottle size: see pictures for bottle size, along with sample bottles that we like; we’re open to any bottle similar to the ones attached.
Current bottles: So ideally, we’d keep the core color on each bottle with a new branding/bottle design. But we're open to your suggestion.

Target Market(s)

mostly women but shouldn't be overly feminine

Requirements
Must have
• see bottle sizes attached

```html
<!DOCTYPE html>
<html lang="en">
<head>
<meta charset="utf-8">
<title>VELQO Dietary Supplement Range</title>
<link rel="stylesheet" href="https://fonts.googleapis.com/css2?family=Montserrat:wght@300;600&display=swap">
<style>
  :root {
    --canvas-bg: #f1f1f1;
    --cap: #0b0b0b;
    --ink: #ffffff;

    --renew-edge: #b25aa6;
    --renew-core: #840a6c;
    --digest-edge: #f28aa2;
    --digest-core: #e52a52;
    --balance-edge: #8bbf7f;
    --balance-core: #35892b;
    --glucose-edge: #7f9be3;
    --glucose-core: #3461d2;
  }

  * { margin: 0; padding: 0; box-sizing: border-box; }

  html, body {
    width: 1200px;
    height: 637px;
    overflow: hidden;
  }

  body {
    background: var(--canvas-bg);
    font-family: "Montserrat", sans-serif;
  }

  .range {
    position: relative;
    width: 1200px;
    height: 637px;
  }

  .label {
    position: absolute;
    top: 130px;
    width: 214px;
    height: 372px;
    overflow: visible;
  }
  .label--renew   { left: 91px; }
  .label--digest  { left: 355px; }
  .label--balance { left: 620px; }
  .label--glucose { left: 884px; }

  .label__cap { fill: var(--cap); }

  .label__category,
  .label__tagline {
    font-family: "Montserrat", sans-serif;
    font-weight: 300;
    font-size: 13px;
    fill: var(--ink);
  }

  .label__brand {
    font-family: "Montserrat", sans-serif;
    font-weight: 300;
    font-size: 50px;
    fill: var(--ink);
  }

  .label__product {
    font-family: "Montserrat", sans-serif;
    font-weight: 300;
    font-size: 21px;
    fill: var(--ink);
  }

  .label__count {
    font-family: "Montserrat", sans-serif;
    font-weight: 600;
    font-size: 8.5px;
    fill: var(--ink);
  }

  .label__rule { stroke: var(--ink); stroke-width: 0.8; }

  .stop-renew-edge   { stop-color: var(--renew-edge); }
  .stop-renew-core   { stop-color: var(--renew-core); }
  .stop-digest-edge  { stop-color: var(--digest-edge); }
  .stop-digest-core  { stop-color: var(--digest-core); }
  .stop-balance-edge { stop-color: var(--balance-edge); }
  .stop-balance-core { stop-color: var(--balance-core); }
  .stop-glucose-edge { stop-color: var(--glucose-edge); }
  .stop-glucose-core { stop-color: var(--glucose-core); }
</style>
</head>
<body>
<main class="range">

  <svg class="label label--renew" viewBox="0 0 214 372" xmlns="http://www.w3.org/2000/svg">
    <defs>
      <linearGradient id="body-renew" x1="0" x2="1" y1="0" y2="0">
        <stop offset="0" class="stop-renew-edge"/>
        <stop offset="0.3" class="stop-renew-core"/>
        <stop offset="0.75" class="stop-renew-core"/>
        <stop offset="1" class="stop-renew-edge"/>
      </linearGradient>
    </defs>
    <rect class="label__cap" x="0" y="0" width="214" height="61"/>
    <rect x="0" y="61" width="214" height="311" fill="url(#body-renew)" role="img" aria-label="Soft-focus capsules visible through the bottle"/>
    <text class="label__category" x="26" y="111">Dietary</text>
    <text class="label__category" x="26" y="123">Supplement</text>
    <text class="label__product" text-anchor="end" transform="translate(149 97) rotate(-90)">Renew</text>
    <text class="label__brand" text-anchor="end" textLength="176" lengthAdjust="spacing" transform="translate(189 97) rotate(-90)">VELQO</text>
    <text class="label__tagline" x="31" y="293">Restoring</text>
    <text class="label__tagline" x="31" y="305">Cleanse &amp; Renewal</text>
    <text class="label__tagline" x="31" y="317">Blend*</text>
    <line class="label__rule" x1="24" y1="340" x2="86" y2="340"/>
    <text class="label__count" x="189" y="343" text-anchor="end">120 Vegetable Capsules</text>
  </svg>

  <svg class="label label--digest" viewBox="0 0 214 372" xmlns="http://www.w3.org/2000/svg">
    <defs>
      <linearGradient id="body-digest" x1="0" x2="1" y1="0" y2="0">
        <stop offset="0" class="stop-digest-edge"/>
        <stop offset="0.3" class="stop-digest-core"/>
        <stop offset="0.75" class="stop-digest-core"/>
        <stop offset="1" class="stop-digest-edge"/>
      </linearGradient>
    </defs>
    <rect class="label__cap" x="0" y="0" width="214" height="61"/>
    <rect x="0" y="61" width="214" height="311" fill="url(#body-digest)" role="img" aria-label="Soft-focus capsules visible through the bottle"/>
    <text class="label__category" x="26" y="111">Dietary</text>
    <text class="label__category" x="26" y="123">Supplement</text>
    <text class="label__product" text-anchor="end" transform="translate(149 97) rotate(-90)">Digest</text>
    <text class="label__brand" text-anchor="end" textLength="176" lengthAdjust="spacing" transform="translate(189 97) rotate(-90)">VELQO</text>
    <text class="label__tagline" x="31" y="293">Gentle Daily</text>
    <text class="label__tagline" x="31" y="305">Digestive Reset*</text>
    <line class="label__rule" x1="24" y1="340" x2="86" y2="340"/>
    <text class="label__count" x="189" y="343" text-anchor="end">120 Vegetable Capsules</text>
  </svg>

  <svg class="label label--balance" viewBox="0 0 214 372" xmlns="http://www.w3.org/2000/svg">
    <defs>
      <linearGradient id="body-balance" x1="0" x2="1" y1="0" y2="0">
        <stop offset="0" class="stop-balance-edge"/>
        <stop offset="0.3" class="stop-balance-core"/>
        <stop offset="0.75" class="stop-balance-core"/>
        <stop offset="1" class="stop-balance-edge"/>
      </linearGradient>
    </defs>
    <rect class="label__cap" x="0" y="0" width="214" height="61"/>
    <rect x="0" y="61" width="214" height="311" fill="url(#body-balance)" role="img" aria-label="Soft-focus capsules visible through the bottle"/>
    <text class="label__category" x="28" y="111">Dietary</text>
    <text class="label__category" x="28" y="123">Supplement</text>
    <text class="label__product" text-anchor="end" transform="translate(149 97) rotate(-90)">Balance</text>
    <text class="label__brand" text-anchor="end" textLength="176" lengthAdjust="spacing" transform="translate(189 97) rotate(-90)">VELQO</text>
    <text class="label__tagline" x="34" y="292">Helps Maintain</text>
    <text class="label__tagline" x="34" y="304">Natural Balance*</text>
    <line class="label__rule" x1="26" y1="339" x2="88" y2="339"/>
    <text class="label__count" x="189" y="342" text-anchor="end">60 Vegetable Capsules</text>
  </svg>

  <svg class="label label--glucose" viewBox="0 0 214 372" xmlns="http://www.w3.org/2000/svg">
    <defs>
      <linearGradient id="body-glucose" x1="0" x2="1" y1="0" y2="0">
        <stop offset="0" class="stop-glucose-edge"/>
        <stop offset="0.3" class="stop-glucose-core"/>
        <stop offset="0.75" class="stop-glucose-core"/>
        <stop offset="1" class="stop-glucose-edge"/>
      </linearGradient>
    </defs>
    <rect class="label__cap" x="0" y="0" width="214" height="61"/>
    <rect x="0" y="61" width="214" height="311" fill="url(#body-glucose)" role="img" aria-label="Soft-focus capsules visible through the bottle"/>
    <text class="label__category" x="26" y="111">Dietary</text>
    <text class="label__category" x="26" y="123">Supplement</text>
    <text class="label__product" text-anchor="end" transform="translate(149 97) rotate(-90)">Glucose Care</text>
    <text class="label__brand" text-anchor="end" textLength="176" lengthAdjust="spacing" transform="translate(189 97) rotate(-90)">VELQO</text>
    <text class="label__tagline" x="31" y="292">Helps Maintain</text>
    <text class="label__tagline" x="31" y="304">Steady Glucose Levels*</text>
    <line class="label__rule" x1="24" y1="339" x2="86" y2="339"/>
    <text class="label__count" x="189" y="342" text-anchor="end">60 Vegetable Capsules</text>
  </svg>

</main>
</body>
</html>
```